Pinevale Harbor Insurance Group, LLC

Design a marketing postcard that we can email to businesses. We want our paperless online cloud based Human Resources system to appear easy and simple to use. www.PinevaleHarborInsurance.example

Please visit these web pages to learn more about how we are bundling all services into One Simple Cloud Solution:
www.brightdeskhub.example
www.gildwagesys.example/solutions/gildwagesys
https://www.videoshare.example/watch?v=Qp3Lx81TnaB&feature=vs.be

Target Market(s)

Small Business HR/Admin Staff.

Industry/Entity Type

Insurance

Logo Text

Pinevale Harbor Insurance

Font styles to use
Sans Serif

Colors

Designer to choose colors to be used in the design.

Requirements
Must have
• "One Simple Cloud Based Solution"
• HR Info System
• Benefits Administration
• Payroll Solutions
• TimeCard Solutions
• Onboarding
• Workers Comp
• ACA Compliance
• Please be sure to include this info on the back:
• 949.571.4026
• Service@PinevaleHarborInsurance.example
• 41562 Calle Bonita
• Suite 312
• Mission Viejo, CA 92691
• www.PinevaleHarborInsurance.example
• CA License # 7K31590
Nice to have
• design postcard with our logo in the center of the postcard like the hub of a wheel and the spokes connecting puffy clouds or pie chart with our solutions.
• Business people photo or background image.
Should not have
• no dark backgrounds. No family photos.

```html
<!DOCTYPE html>
<html lang="en">
<head>
<meta charset="utf-8">
<title>Pinevale Harbor Insurance – HR &amp; Benefits Postcard</title>
<link rel="stylesheet" href="https://fonts.googleapis.com/css2?family=Catamaran:wght@400;500;600;700&display=swap">
<style>
  :root {
    --navy: #1d3f63;
    --gold: #ecbe1d;
    --ink: #1f1f1f;
    --white: #ffffff;
    --page: #eeeeec;
    --line: #55606b;
    --photo-dark: #2e3948;
    --photo-mid: #6d7d90;
    --photo-light: #dfe3e8;
  }
  * { box-sizing: border-box; margin: 0; padding: 0; }
  html, body {
    width: 1200px; height: 1000px; overflow: hidden;
    background: var(--page);
    font-family: "Catamaran", Arial, sans-serif;
    color: var(--ink);
  }
  .sheet { position: relative; width: 1200px; height: 1000px; }
  .postcard {
    position: absolute; left: 240px; width: 720px; height: 480px;
    background: var(--white);
    box-shadow: 0 4px 14px rgba(0,0,0,.18);
    overflow: hidden;
  }
  .postcard--back { top: 14px; }
  .postcard--front { top: 506px; }

  /* ---------- back ---------- */
  .back-photo {
    position: absolute; inset: 0;
    background: linear-gradient(100deg, var(--photo-light) 40%, #c9cfd7 60%, #b8c0ca 75%, var(--photo-light) 100%);
    opacity: .9;
  }
  .solutions {
    position: absolute; left: 0; top: 0; width: 340px; height: 100%;
    background: var(--gold);
  }
  .solutions__title {
    background: var(--navy); color: var(--white);
    font-weight: 700; font-size: 21px; line-height: 1.2;
    text-transform: uppercase; letter-spacing: .3px;
    padding: 26px 22px 20px;
  }
  .solutions__list { padding: 18px 22px; }
  .solution { margin-bottom: 8px; }
  .solution__name {
    font-weight: 700; font-size: 17px; line-height: 1.35; color: var(--navy);
    text-decoration: underline; text-underline-offset: 3px;
  }
  .solution__text { font-size: 14px; line-height: 1.35; color: #3a3a3a; }
  .postage {
    position: absolute; right: 24px; top: 22px; width: 112px; height: 122px;
    border: 1.5px solid var(--line);
    font-size: 14px; color: #444; text-align: center; padding-top: 14px;
  }
  .address-lines { position: absolute; left: 380px; right: 24px; top: 210px; }
  .address-lines span { display: block; height: 44px; border-bottom: 1.5px solid var(--line); }

  /* ---------- front ---------- */
  .brand {
    position: absolute; left: 0; right: 0; top: 0; height: 108px;
    display: flex; align-items: center; justify-content: center; gap: 10px;
  }
  .brand__dot { width: 26px; height: 26px; border-radius: 50%; background: var(--navy); }
  .brand__name { font-size: 24px; font-weight: 600; color: var(--navy); }
  .front-photo {
    position: absolute; left: 0; top: 108px; width: 100%; height: 236px;
    background: linear-gradient(90deg, var(--photo-dark) 0%, var(--photo-mid) 45%, #c7ccd3 70%, var(--photo-dark) 100%);
  }
  .contact-band {
    position: absolute; left: 0; bottom: 0; width: 100%; height: 136px;
    background: var(--gold);
    font-size: 13.5px; line-height: 1.45;
  }
  .contact__address {
    position: absolute; left: 26px; bottom: 22px;
    display: flex; align-items: center; gap: 12px;
  }
  .contact__online { position: absolute; left: 232px; top: 56px; }
  .contact__row { display: flex; align-items: center; gap: 8px; white-space: nowrap; }
  .contact__phone {
    position: absolute; right: 28px; top: 14px;
    display: flex; align-items: center; gap: 12px;
    font-size: 27px; font-weight: 600; letter-spacing: .5px; white-space: nowrap;
  }
  .icon { flex: none; fill: none; stroke: var(--ink); stroke-width: 1.6; }
  .icon--solid { fill: var(--ink); stroke: none; }
</style>
</head>
<body>
<main class="sheet">

  <section class="postcard postcard--back" aria-label="Postcard back">
    <div class="back-photo" role="img" aria-label="Faded photo of a businesswoman in a meeting"></div>
    <div class="solutions">
      <h2 class="solutions__title">One Simple HR &amp; Benefits Cloud Based Solution</h2>
      <div class="solutions__list">
        <div class="solution">
          <p class="solution__name">HR Info System</p>
          <p class="solution__text">Powerful PTO tracking, performance reviews and goal setting for managers.</p>
        </div>
        <div class="solution"><p class="solution__name">Benefits Administration</p></div>
        <div class="solution"><p class="solution__name">Payroll Solutions</p></div>
        <div class="solution"><p class="solution__name">TimeCard Solutions</p></div>
        <div class="solution"><p class="solution__name">Onboarding</p></div>
        <div class="solution"><p class="solution__name">Workers Comp</p></div>
        <div class="solution"><p class="solution__name">ACA Compliance</p></div>
      </div>
    </div>
    <div class="postage">Postage</div>
    <div class="address-lines"><span></span><span></span><span></span><span></span><span></span></div>
  </section>

  <section class="postcard postcard--front" aria-label="Postcard front">
    <header class="brand">
      <span class="brand__dot"></span>
      <span class="brand__name">Pinevale Harbor Insurance</span>
    </header>
    <div class="front-photo" role="img" aria-label="Photo of office staff working at computer screens"></div>
    <footer class="contact-band">
      <div class="contact__address">
        <svg class="icon icon--solid" width="14" height="20" viewBox="0 0 14 20"><path d="M7 0a7 7 0 0 0-7 7c0 5 7 13 7 13s7-8 7-13a7 7 0 0 0-7-7zm0 9.5A2.5 2.5 0 1 1 7 4.5a2.5 2.5 0 0 1 0 5z"/></svg>
        <p>41562 Calle Bonita<br>Suite 312<br>Mission Viejo, CA 92691</p>
      </div>
      <div class="contact__online">
        <p class="contact__row">
          <svg class="icon" width="16" height="14" viewBox="0 0 16 14"><path d="M1 7 8 1l7 6M3 5.5V13h10V5.5"/></svg>
          www.PinevaleHarborInsurance.example
        </p>
        <p class="contact__row">
          <svg class="icon" width="16" height="12" viewBox="0 0 16 12"><rect x="1" y="1" width="14" height="10"/><path d="m1 1 7 6 7-6"/></svg>
          Service@PinevaleHarborInsurance.example
        </p>
        <p class="contact__row">
          <svg class="icon" width="16" height="12" viewBox="0 0 16 12"><rect x="1" y="1" width="14" height="10"/><path d="M4 5h5M4 8h8"/></svg>
          CA License # 7K31590
        </p>
      </div>
      <p class="contact__phone">
        <svg class="icon icon--solid" width="26" height="26" viewBox="0 0 24 24"><path d="M6.6 10.8a15.1 15.1 0 0 0 6.6 6.6l2.2-2.2a1 1 0 0 1 1-.25 11.4 11.4 0 0 0 3.6.57 1 1 0 0 1 1 1V20a1 1 0 0 1-1 1A17 17 0 0 1 3 4a1 1 0 0 1 1-1h3.5a1 1 0 0 1 1 1c0 1.25.2 2.45.57 3.570a1 1 0 0 1-.25 1z"/></svg>
        949.571.4026
      </p>
    </footer>
  </section>

</main>
</body>
</html>
```